Business Card

I would like a business card with a picture of my husband and I that is unique and professional.

Industry/Entity Type

Business

Font styles to use
Serif

```html
<!DOCTYPE html>
<html lang="en">
<head>
<meta charset="utf-8">
<title>Mercer Leadership Group – Business Card</title>
<link rel="stylesheet" href="https://fonts.googleapis.com/css2?family=Oswald:wght@500&display=swap">
<style>
  :root {
    --stage: #1c1c1d;
    --card-dark: #2b2b2c;
    --card-light: #f4f4f4;
    --band: #2a2a2a;
    --bar: #1b1b1b;
    --gold: #d9a23a;
    --gold-soft: #b98a3a;
    --photo-a: #c9c9cc;
    --photo-b: #6d6d72;
  }
  * { box-sizing: border-box; margin: 0; padding: 0; }
  html, body { width: 1200px; height: 900px; overflow: hidden; }
  body {
    background: var(--stage);
    font-family: "Oswald", "Arial Narrow", sans-serif;
    font-weight: 500;
    position: relative;
  }
  .card {
    position: absolute;
    left: 180px;
    width: 840px;
    height: 330px;
    overflow: hidden;
    box-shadow: 0 10px 30px rgba(0,0,0,.5);
  }
  .card-back { top: 70px; background: var(--card-dark); }
  .card-front { top: 480px; background: var(--card-light); }

  .brand {
    position: absolute;
    display: flex;
    align-items: center;
    gap: 12px;
    color: var(--gold);
    text-transform: uppercase;
    letter-spacing: 2px;
    white-space: nowrap;
  }
  .brand-dot {
    width: 18px; height: 18px;
    border-radius: 50%;
    background: var(--gold);
    flex: none;
  }
  .card-back .brand {
    left: 50%; top: 50%;
    transform: translate(-50%, -50%);
    font-size: 26px;
  }
  .card-front .brand {
    left: 44px; bottom: 34px;
    font-size: 16px;
    color: var(--gold-soft);
  }
  .card-front .brand-dot { width: 14px; height: 14px; background: var(--gold-soft); }

  .name-band {
    position: absolute;
    left: 0; top: 0;
    width: 560px; height: 100px;
    background: var(--band);
    padding: 16px 0 0 44px;
    text-transform: uppercase;
    color: var(--gold);
  }
  .person-name { font-size: 34px; letter-spacing: 1px; line-height: 1.1; }
  .person-title { font-size: 20px; letter-spacing: 1px; margin-top: 2px; }

  .photo {
    position: absolute;
    right: 0; top: 0;
    width: 280px; height: 330px;
    background: linear-gradient(160deg, var(--photo-a), var(--photo-b));
  }

  .contact {
    position: absolute;
    right: 260px;
    background: var(--bar);
    color: var(--gold);
    font-size: 22px;
    line-height: 30px;
    letter-spacing: 1px;
    text-transform: uppercase;
    padding: 8px 26px;
    white-space: nowrap;
  }
  .contact-phone { top: 130px; }
  .contact-email { top: 196px; }
</style>
</head>
<body>
  <section class="card card-back" aria-label="Card back">
    <div class="brand"><span class="brand-dot"></span>Mercer Leadership Group</div>
  </section>

  <section class="card card-front" aria-label="Card front">
    <div class="name-band">
      <p class="person-name">Dana Mercer</p>
      <p class="person-title">Professional Mentorship Strategist</p>
    </div>
    <div class="photo" role="img" aria-label="Portrait photo of the couple in business attire"></div>
    <p class="contact contact-phone">555-014-2287</p>
    <p class="contact contact-email">danamercer@example.com</p>
    <div class="brand"><span class="brand-dot"></span>Mercer Leadership Group</div>
  </section>
</body>
</html>
```